Corvel Ridge New Website Design

We just changed our logo (thank you PlanHarbor) and company name change from Corvel Ridge Machining to Corvel Ridge Manufacturing. We do CNC Swiss screw machining and multi-axis machines. We make parts for many industries. We make large quantity production parts as well small R&D quantities. You can look at our current (outdated) website: http://www.corvelridgemachining.example to see what we do. We would like a WordPress site, including contact form for "request for quote" . We would also like it to be mobile friendly, and the ability to maintain it ourselves after it is finished I have included our new logo and fonts for references. We would like our site to convey the feeling of precision, capability, and trust worthiness with a very modern look. The new website address is www.corvelridge-mfg.example

Coding

Coded - Design and coding required

Number of Pages Required

5+ page

Font styles to use
Serif
Sans Serif
Other font styles liked:
• fronts included, not sure if they work

Colors

Designer to choose colors to be used in the design.

Requirements
Must have
• Contact Info, request for quote field

```html
<!DOCTYPE html>
<html lang="en">
<head>
<meta charset="utf-8">
<title>Corvel Ridge Manufacturing</title>
<link href="https://fonts.googleapis.com/css2?family=Orbitron:wght@500;600&family=Barlow:wght@400;500;600;700&display=swap" rel="stylesheet">
<style>
:root{
  --navy:#1d3a8a;
  --navy-dark:#16306f;
  --ink:#222831;
  --text:#555b66;
  --white:#ffffff;
  --steel-dark:#1f2630;
  --steel:#3a4552;
  --hero-a:#2a323d;
  --hero-b:#4d5866;
  --strip:rgba(12,16,22,.72);
  --blue-photo-a:#2f56a6;
  --blue-photo-b:#4a70bd;
  --denim:#2a4d9a;
  --yellow:#f2cf2a;
  --footer-a:#3c4148;
  --footer-b:#5a5f66;
  --line:#d7dbe2;
}
*{box-sizing:border-box;margin:0;padding:0}
html,body{width:1200px;height:3371px;overflow:hidden}
body{font-family:"Barlow",Arial,sans-serif;color:var(--text);background:var(--white);position:relative}
.abs{position:absolute}
.display{font-family:"Orbitron","Barlow",sans-serif}

/* header */
.site-header{left:0;top:0;width:1200px;height:120px;background:var(--white)}
.brand{left:58px;top:16px;display:flex;align-items:center;gap:12px}
.brand-dot{width:40px;height:40px;border-radius:50%;background:var(--navy)}
.brand-name{font-weight:700;color:var(--navy);font-size:22px;line-height:24px;letter-spacing:1px;text-transform:uppercase}
.header-call{left:688px;top:22px;font-size:21px;color:var(--ink)}
.header-call strong{color:var(--navy);font-weight:600}
.quote-btn{left:940px;top:19px;width:201px;height:34px;border:2px solid #9aa3b0;border-radius:17px;font-size:13px;font-weight:600;letter-spacing:1px;color:var(--navy);display:flex;align-items:center;justify-content:center}
.main-nav{left:348px;top:79px;width:852px;height:41px;background:var(--navy)}
.main-nav ul{list-style:none;display:flex;height:100%}
.main-nav li{flex:1;display:flex;align-items:center;justify-content:center;color:var(--white);font-size:13px;font-weight:700;letter-spacing:1px;border-left:2px solid rgba(255,255,255,.35);transform:skewX(-30deg)}
.main-nav li span{transform:skewX(30deg)}
.main-nav li:first-child{border-left:none;background:var(--navy-dark)}

/* hero (children positioned relative to hero) */
.hero{left:0;top:120px;width:1200px;height:480px;background:linear-gradient(120deg,var(--hero-a),var(--hero-b) 55%,#2b323b)}
.hero-box{left:240px;top:161px;width:720px;height:157px;border:2px solid rgba(255,255,255,.85)}
.hero-title{left:240px;top:125px;width:720px;text-align:center;color:var(--white);font-size:30px;line-height:36px;font-weight:500;letter-spacing:1px}
.search{left:281px;top:233px;width:640px;height:47px;display:flex}
.search-field{flex:1;background:var(--white);display:flex;align-items:center;padding-left:16px;font-size:13px;color:#9aa0a8}
.search-btn{width:177px;background:var(--navy);color:var(--white);font-size:13px;font-weight:700;letter-spacing:1px;display:flex;align-items:center;justify-content:center}
.served{left:0;top:372px;width:1200px;text-align:center;color:var(--white);font-size:13px;font-weight:700;letter-spacing:1px}
.served svg{display:block;margin:10px auto 0}
.industries{left:0;top:600px;width:1200px;height:238px;background:linear-gradient(120deg,#1b2029,#262d36 50%,#171b22)}
.industry{top:88px;width:130px;text-align:center;color:var(--white);font-size:16px}
.industry svg{display:block;margin:0 auto 10px}
.carousel-arrow{top:104px}

/* about */
.about-title{left:0;top:910px;width:1200px;text-align:center;color:var(--navy);font-size:29px;line-height:37px;font-weight:500;letter-spacing:1px}
.about-photo{left:240px;top:1013px;width:241px;height:239px;background:linear-gradient(135deg,#3c5068,#8fa6c0 50%,#2d3948)}
.about-text{left:544px;top:1008px;width:412px;font-size:13px;line-height:20px;color:var(--text)}
.about-text p+p{margin-top:18px}
.outline-btn{border:1.5px solid #7b838f;color:var(--ink);font-size:12px;font-weight:700;letter-spacing:1px;display:flex;align-items:center;justify-content:center;text-transform:uppercase}
.about-btn{left:544px;top:1220px;width:159px;height:32px}

/* services */
.services{left:0;top:1333px;width:1200px;height:359px;background:linear-gradient(120deg,var(--steel-dark),var(--steel) 50%,#27303a)}
.services-title{left:0;top:74px;width:1200px;text-align:center;color:var(--white);font-size:28px;font-weight:500;letter-spacing:1px}
.services-text{left:180px;top:122px;width:840px;text-align:center;color:#e6e9ee;font-size:14px;line-height:20px}
.light-btn{left:519px;top:247px;width:160px;height:32px;border:1.5px solid rgba(255,255,255,.8);color:var(--white);font-size:12px;font-weight:700;letter-spacing:1px;display:flex;align-items:center;justify-content:center}

/* equipment */
.equipment-title{left:0;top:1764px;width:1200px;text-align:center;color:var(--navy);font-size:36px;font-weight:500;letter-spacing:1px}
.card{top:1840px;width:304px}
.card-photo{height:200px}
.card-photo.support{background:linear-gradient(135deg,#d9531e,#7a7e84 60%,#3b3f45)}
.card-photo.qa{background:linear-gradient(135deg,#5b5e60,#b9b7ad 50%,#3e4042)}
.card-photo.machining{background:linear-gradient(135deg,#8f969c,#cfd3d6 50%,#6a7176)}
.card h3{margin-top:22px;font-size:19px;font-weight:600;color:var(--ink)}
.card hr{border:0;border-top:1px solid var(--line);width:62px;margin:10px 0 14px}
.card p{font-size:13px;line-height:20px;color:var(--text);height:60px}
.card .outline-btn{margin-top:28px;width:130px;height:30px}
.card .outline-btn.filled{background:var(--navy);border-color:var(--navy);color:var(--white)}

/* testimonials */
.testimonials{left:0;top:2310px;width:1200px;height:425px;background:linear-gradient(120deg,var(--blue-photo-a),var(--blue-photo-b) 55%,#2f55a4)}
.testimonials-title{left:0;top:72px;width:1200px;text-align:center;color:var(--white);font-size:34px;font-weight:500;letter-spacing:1px}
.quote{left:280px;top:144px;width:640px;text-align:center;color:var(--white);font-size:20px;line-height:28px}
.quote .mark{color:var(--yellow);font-weight:700}
.avatar{left:570px;top:237px;width:60px;height:60px;border-radius:50%;background:linear-gradient(#c9b39a,#7d6a58);border:3px solid var(--white)}
.person{left:0;top:308px;width:1200px;text-align:center;color:var(--white)}
.person b{display:block;font-size:15px;font-weight:700}
.person span{font-size:13px}

/* newsletter */
.newsletter{left:0;top:2735px;width:1200px;height:121px;background:var(--denim)}
.newsletter h2{left:119px;top:28px;font-family:"Orbitron","Barlow",sans-serif;color:var(--yellow);font-size:24px;font-weight:500}
.newsletter p{left:119px;top:66px;color:#dfe6f4;font-size:15px}
.signup{left:719px;top:29px;width:360px;height:60px;background:var(--white);border-radius:30px;display:flex;align-items:center;padding:0 10px 0 30px;gap:14px;font-size:15px;color:#9aa0a8}
.signup span{flex:1}
.signup-btn{width:99px;height:38px;border-radius:19px;background:#2e3542;color:var(--white);font-size:12px;font-weight:700;letter-spacing:1px;display:flex;align-items:center;justify-content:center}

/* footer */
.site-footer{left:0;top:2856px;width:1200px;height:515px;background:linear-gradient(120deg,var(--footer-a),var(--footer-b) 50%,#3e434a);color:var(--white)}
.footer-h{font-size:20px;line-height:24px;font-weight:600}
.field{height:39px;border:1.5px solid rgba(255,255,255,.6);font-size:13px;color:#e3e5e8;padding:10px 16px}
.send-btn{left:240px;top:387px;width:171px;height:35px;background:var(--navy);font-size:12px;font-weight:700;letter-spacing:1px;display:flex;align-items:center;justify-content:center}
.footer-rule{left:119px;top:362px;width:960px;border-top:1px solid rgba(255,255,255,.35)}
.contact-call{left:719px;top:138px;font-size:16px;line-height:22px;font-weight:600;color:var(--white)}
.contact-info{left:719px;top:180px;font-size:14px;line-height:22px;color:#eceef1}
.socials{left:719px;top:302px;display:flex;gap:12px}
.socials i{display:block;width:16px;height:16px;border:1.5px solid #e3e5e8;border-radius:3px}
.copyright{left:719px;top:380px;font-size:13px;line-height:22px;color:#e3e5e8}
.to-top{left:1131px;top:350px}
</style>
</head>
<body>

<header class="site-header abs">
  <div class="brand abs"><div class="brand-dot"></div><div class="brand-name">Corvel Ridge<br>Manufacturing</div></div>
  <div class="header-call abs">Call Us. <strong>858-555-0172</strong></div>
  <div class="quote-btn abs">GET FREE QUOTES</div>
  <nav class="main-nav abs">
    <ul>
      <li><span>ABOUT US</span></li><li><span>SERVICES</span></li><li><span>EQUIPMENT</span></li><li><span>QUALITY</span></li><li><span>OUR WORK</span></li><li><span>CONTACT US</span></li>
    </ul>
  </nav>
</header>

<section class="hero abs" role="img" aria-label="Close-up photograph of a CNC machining centre in dark steel tones">
  <div class="hero-box abs"></div>
  <h1 class="hero-title display abs">From Blueprint to Reality<br>Better Than you Expected</h1>
  <div class="search abs">
    <div class="search-field">Search by Equipment Type, Model or Manufacturer</div>
    <div class="search-btn">CLICK TO SEARCH</div>
  </div>
  <div class="served abs">INDUSTRIES WE SERVED
    <svg width="14" height="18" viewBox="0 0 14 18"><path d="M7 1v15M2 11l5 5 5-5" fill="none" stroke="#fff" stroke-width="1.6"/></svg>
  </div>
</section>

<div class="industries abs">
  <svg class="carousel-arrow abs" style="left:58px" width="16" height="28" viewBox="0 0 16 28"><path d="M13 2L3 14l10 12" fill="none" stroke="#fff" stroke-width="2"/></svg>
  <svg class="carousel-arrow abs" style="left:1124px" width="16" height="28" viewBox="0 0 16 28"><path d="M3 2l10 12L3 26" fill="none" stroke="#fff" stroke-width="2"/></svg>
  <div class="industry abs" style="left:153px">
    <svg width="46" height="46" viewBox="0 0 46 46" fill="none" stroke="#fff" stroke-width="2"><path d="M6 30l12-4 14-16c3-3 7-1 4 3L22 28l-4 12-3 0 0-10-7 2z"/></svg>Aerospace</div>
  <div class="industry abs" style="left:344px">
    <svg width="46" height="46" viewBox="0 0 46 46" fill="none" stroke="#fff" stroke-width="2"><circle cx="23" cy="23" r="19"/><circle cx="23" cy="23" r="5"/><path d="M5 20h13M28 20h13M23 28v14"/></svg>Automotive</div>
  <div class="industry abs" style="left:533px">
    <svg width="46" height="46" viewBox="0 0 46 46" fill="none" stroke="#fff" stroke-width="2"><rect x="4" y="7" width="38" height="26" rx="2"/><path d="M17 40h12M23 33v7"/></svg>Computer</div>
  <div class="industry abs" style="left:724px">
    <svg width="46" height="46" viewBox="0 0 46 46" fill="none" stroke="#fff" stroke-width="2"><path d="M12 6c-6 2-6 12-2 18 2 5 2 16 6 16s3-10 7-10 3 10 7 10 4-11 6-16c4-6 4-16-2-18-4-1-7 2-11 2s-7-3-11-2z"/></svg>Dental</div>
  <div class="industry abs" style="left:915px">
    <svg width="46" height="46" viewBox="0 0 46 46" fill="none" stroke="#fff" stroke-width="2"><circle cx="23" cy="20" r="14"/><path d="M17 38h12M19 42h8M20 22l3-6 3 6"/></svg>Electronics</div>
</div>

<section class="about">
  <h2 class="about-title display abs">Founded in 1996,<br>Corvel Ridge Manufacturing Inc.</h2>
  <div class="about-photo abs" role="img" aria-label="Photograph of a milling tool cutting metal with coolant spray"></div>
  <div class="about-text abs">
    <p>Corvel Ridge Machining Company is a high quality machining resource providing friendly service, fast turnaround times, and engineering expertise, at competitive pricing. With almost 20 years of experience in the industry, Corvel Ridge utilizes certified state of the art equipment partnered with top professionals to maximize the value and quality in your product.</p>
    <p>Specializing in precision, Corvel Ridge will provide you with superior products, at affordable prices.</p>
  </div>
  <div class="about-btn outline-btn abs">Discover About Us</div>
</section>

<section class="services abs" role="img" aria-label="Dark background photograph of precision machining equipment">
  <h2 class="services-title display abs">Service Offering</h2>
  <p class="services-text abs">Providing you with honest straightforward service is our number one goal. We manufacture finished metal and plastic goods to tight tolerances using technologically advanced equipment. Our spotlight is multi-featured products manufactured on 7 plus axis world-class screw machines. Our ideal sizes, not our limits, are from .02 to 1.25 inches diameter by .050 to 5.00 inches in length. Cross holes, wrench flats or something new to us all, completed in one operation. Whether you need to make one or a million our screw machine department is capable of fulfilling your need.</p>
  <div class="light-btn abs">EXPLORE MORE</div>
</section>

<section class="equipment">
  <h2 class="equipment-title display abs">Our Equipment</h2>
  <article class="card abs" style="left:119px">
    <div class="card-photo support" role="img" aria-label="Photograph of an orange band saw"></div>
    <h3>Support Equipment</h3><hr>
    <p>There are many variations of passages of Lorem Ipsum available, but the majority have suffere alteration in some form ...</p>
    <div class="outline-btn">Read More</div>
  </article>
  <article class="card abs" style="left:447px">
    <div class="card-photo qa" role="img" aria-label="Photograph of an optical comparator for inspection"></div>
    <h3>Qa Equipment</h3><hr>
    <p>There are many variations of passages of Lorem Ipsum available, but the majority have suffere alteration in some form ...</p>
    <div class="outline-btn filled">Read More</div>
  </article>
  <article class="card abs" style="left:775px">
    <div class="card-photo machining" role="img" aria-label="Photograph of a row of Swiss screw machines on a shop floor"></div>
    <h3>Machining Equipment</h3><hr>
    <p>Kestrel Dynamo 7 plus axis machining at its best. Part to print milling and turning in one operation. Your part comes off complete ...</p>
    <div class="outline-btn">Read More</div>
  </article>
</section>

<section class="testimonials abs" role="img" aria-label="Blue tinted photograph of machine gears">
  <h2 class="testimonials-title display abs">Testimonials</h2>
  <p class="quote abs"><span class="mark">&ldquo;</span> I love working with engineers. Finding ways to make their parts less expensive is a puzzle I never get tired of solving. <span class="mark">&rdquo;</span></p>
  <div class="avatar abs" role="img" aria-label="Portrait of the founder"></div>
  <div class="person abs"><b>Daniel Orsett</b><span>Founder</span></div>
</section>

<section class="newsletter abs">
  <h2 class="abs">New Equipment Email Notification</h2>
  <p class="abs">Subscribe to get instant notification in your email inbox.</p>
  <div class="signup abs">
    <svg width="20" height="15" viewBox="0 0 20 15" fill="none" stroke="#2e3542" stroke-width="1.5"><rect x="1" y="1" width="18" height="13"/><path d="M1 1l9 7 9-7"/></svg>
    <span>name@email.com</span>
    <div class="signup-btn">SIGN UP</div>
  </div>
</section>

<footer class="site-footer abs" role="img" aria-label="Grey photograph of machine gears">
  <h3 class="footer-h abs" style="left:240px;top:110px">Get Free Quotes</h3>
  <div class="field abs" style="left:240px;top:152px;width:171px">Your Name</div>
  <div class="field abs" style="left:434px;top:152px;width:166px">Email</div>
  <div class="field abs" style="left:240px;top:209px;width:171px">Phone</div>
  <div class="field abs" style="left:434px;top:209px;width:166px">Subject</div>
  <div class="field abs" style="left:240px;top:265px;width:360px;height:94px">Message ..</div>
  <div class="footer-rule abs"></div>
  <div class="send-btn abs">SEND MESSAGE</div>

  <h3 class="footer-h abs" style="left:719px;top:110px">Have any Questions?</h3>
  <div class="contact-call abs">Call Us. 858-555-0172</div>
  <div class="contact-info abs">Corvel Ridge Manufacturing Inc.<br>4410 Halvern Ct. Lakemont,<br>CA 90000</div>
  <div class="socials abs"><i></i><i></i><i></i><i></i></div>
  <svg class="to-top abs" width="16" height="20" viewBox="0 0 16 20"><path d="M8 18V3M3 8l5-5 5 5" fill="none" stroke="#f2cf2a" stroke-width="1.6"/></svg>
  <div class="copyright abs">&copy; 2019 Corvel Ridge Manufacturing Inc.<br>All Rights Reserved.</div>
</footer>

</body>
</html>
```